The Kettlebrook

We need a menu design for our restaurant. Our current menu was designed by us and is ok - but we would like something more... The current lay out is in a tri-fold 8x11 - we want to keep the to a standard paper size but would like to make it larger so the menu items stand out more (maybe double sided 6x11 or double sided 8x11). Ideally, we'd like to have a design where we can edit the text accordingly, as our menu choices change regularly. The feel of the restaurant is casual and rustic. We specialize in Craft Beers, Wings and Burritos - everything is homemade and made fresh daily - we'd like the menu to be more 'user friendly'. Our Burritos are made to order. A customer chooses their meat then adds toppings. Because of our currently lay out - descriptions are small and flow is not great. I'd also like to add some appropriate graphics to make it more appealing. We are in family restaurant in a resort town and cater to skiers, mountain bikers, hikers hunters, fisherman, ect...the atmosphere is casual, eclectic, and rustic with a bit of a "hippy" vibe for lack of better term. Always good music, good food, good times...
Target Market(s)
We cater to Locals (hunters/country/"simple folk") AND Tourists (hipster "city slickers") who visit the area. We have a niche where we successfully cater to both because we are not too much one or the other. We are relatable to both and the menu feel should reflect the same.
Industry/Entity Type
Restaurant
Requirements
Must have
- Text of file must be editable by us once final design is received. We need to be able to update the text of menu accordingly.
- Kettlebrook logo.
Nice to have
- More graphics, better fonts (fonts should be fun/casual)

```html
<!DOCTYPE html>
<html lang="en">
<head>
<meta charset="utf-8">
<title>The Kettlebrook – Menu</title>
<link rel="stylesheet" href="https://fonts.googleapis.com/css2?family=Courgette&family=Roboto+Condensed:wght@400;700&family=Lora:ital,wght@1,700&display=swap">
<style>
  :root {
    --wood-light: #efe1cb;
    --wood-mid: #e6d3b6;
    --wood-dark: #d9c3a2;
    --red: #c8202b;
    --red-dark: #961820;
    --red-text: #d31f2b;
    --ink: #4a3b30;
    --gold: #f5c842;
    --cream: #fff6e2;
  }
  * { box-sizing: border-box; margin: 0; padding: 0; }
  html, body { width: 1200px; height: 848px; overflow: hidden; background: #fff; }
  .menu {
    position: relative; width: 1200px; height: 848px; overflow: hidden;
    font-family: "Roboto Condensed", Arial, sans-serif; color: var(--ink);
  }
  .wood-texture {
    position: absolute; inset: 0;
    background: linear-gradient(100deg, var(--wood-light) 0%, var(--wood-mid) 45%, var(--wood-light) 70%, var(--wood-dark) 100%);
  }
  .ribbon { position: absolute; height: 54px; }
  .ribbon svg { position: absolute; inset: 0; width: 100%; height: 100%; }
  .ribbon span {
    position: absolute; inset: 0; display: flex; align-items: center; justify-content: center;
    font-family: "Courgette", cursive; font-size: 26px; color: #fff; padding-bottom: 4px;
  }
  .section-title { position: absolute; font-weight: 700; font-size: 23px; color: var(--ink); }
  .price-badge {
    position: absolute; width: 25px; height: 25px; border-radius: 50%;
    background: var(--red); color: #fff; font-weight: 700; font-size: 16px;
    display: flex; align-items: center; justify-content: center;
    box-shadow: 0 0 0 2px var(--cream) inset;
  }
  .row {
    position: absolute; display: flex; justify-content: space-between;
    font-weight: 700; font-size: 18px; line-height: 1;
  }
  .level { position: absolute; font-weight: 700; font-size: 17px; }
  .level b { color: var(--red-text); }
  .note { position: absolute; font-size: 14px; line-height: 1.35; }
  .desc { position: absolute; font-size: 11px; line-height: 1.3; width: 320px; }
  .plaque { position: absolute; }
  .plaque svg { position: absolute; inset: 0; width: 100%; height: 100%; }
  .plaque p {
    position: absolute; inset: 0; display: flex; align-items: center; justify-content: center; text-align: center;
    font-family: "Lora", Georgia, serif; font-style: italic; font-weight: 700; color: var(--gold);
  }
  .brand {
    position: absolute; left: 422px; top: 120px; width: 348px;
    display: flex; align-items: center; justify-content: center; gap: 12px;
  }
  .brand-mark { width: 22px; height: 22px; border-radius: 50%; background: var(--ink); flex: none; }
  .brand-name {
    font-family: "Roboto Condensed", Arial, sans-serif; font-weight: 700; font-size: 34px;
    color: var(--ink); white-space: nowrap;
  }
  .hours { position: absolute; left: 422px; top: 224px; width: 348px; text-align: center; }
  .hours h3 { color: var(--red-text); font-size: 17px; font-weight: 700; border-bottom: 1.5px solid var(--red-text); display: inline-block; padding: 0 6px 2px; }
  .hours p { font-weight: 700; font-size: 17px; line-height: 1.3; margin-top: 4px; }
  .intro { position: absolute; left: 422px; top: 368px; width: 348px; text-align: center; }
  .intro p { font-size: 13px; }
  .intro .fresh { font-family: "Lora", Georgia, serif; font-style: italic; font-weight: 700; color: var(--red-text); font-size: 18px; margin-top: 2px; }
  .list { position: absolute; font-weight: 700; font-size: 17px; line-height: 24px; }
  .list small { display: block; font-weight: 400; font-size: 12px; line-height: 12px; margin-top: -3px; }
  .divider { position: absolute; width: 1.5px; background: var(--ink); }
</style>
</head>
<body>
<div class="menu">
  <div class="wood-texture" role="img" aria-label="Light wooden plank background with faint music note decorations"></div>

  <!-- Wings column -->
  <div class="ribbon" style="left:24px; top:52px; width:349px;">
    <svg viewBox="0 0 349 54" preserveAspectRatio="none" aria-hidden="true">
      <polygon points="0,14 40,14 40,50 0,50 12,32" fill="var(--red-dark)"/>
      <polygon points="349,14 309,14 309,50 349,50 337,32" fill="var(--red-dark)"/>
      <path d="M26,4 Q174,14 323,4 L323,42 Q174,52 26,42 Z" fill="var(--red)"/>
    </svg>
    <span>Wings</span>
  </div>

  <div class="price-badge" style="left:335px; top:130px;">$</div>
  <div class="row" style="left:24px; top:162px; width:349px; font-size:20px;"><span>Buffalo Style</span><span>9.00</span></div>
  <div class="level" style="left:24px; top:198px;"><b>Mild:</b> Sweet &amp; Tangy</div>
  <div class="level" style="left:24px; top:226px;"><b>Medium:</b> Bold &amp; Spicy</div>
  <div class="level" style="left:24px; top:254px;"><b>Hot:</b> Teary-Eyed &amp; Sweaty-Browed</div>

  <div class="section-title" style="left:24px; top:312px;">Specialty</div>
  <div class="price-badge" style="left:335px; top:311px;">$</div>
  <div class="row" style="left:24px; top:360px; width:349px;"><span>BBQ</span><span>9.00</span></div>
  <div class="row" style="left:24px; top:388px; width:349px;"><span>Ha-B-Q (hot!)</span><span>11.00</span></div>
  <div class="row" style="left:24px; top:416px; width:349px;"><span>Shanghai Garlic</span><span>11.00</span></div>
  <div class="row" style="left:24px; top:444px; width:349px;"><span>Hot Honey Thai</span><span>11.00</span></div>
  <div class="row" style="left:24px; top:472px; width:349px;"><span>RazbaNero (hot!)</span><span>11.00</span></div>

  <div class="plaque" style="left:24px; top:518px; width:349px; height:54px;">
    <svg viewBox="0 0 349 54" preserveAspectRatio="none" aria-hidden="true">
      <path d="M14,0 H335 L349,14 V40 L335,54 H14 L0,40 V14 Z" fill="var(--red)"/>
      <path d="M17,4 H332 L345,16 V38 L332,50 H17 L4,38 V16 Z" fill="none" stroke="var(--gold)" stroke-width="2"/>
    </svg>
    <p style="font-size:19px;">All Sauces Are Homemade!</p>
  </div>

  <div class="section-title" style="left:24px; top:615px;">Sampler</div>
  <div class="price-badge" style="left:335px; top:612px;">$</div>
  <div class="row" style="left:24px; top:660px; width:349px;"><span>Dozen wings</span><span>15.00</span></div>
  <div class="note" style="left:24px; top:680px;">Mix and match<br>Your choice of 3 flavors (4 wings ea.)</div>

  <div class="plaque" style="left:24px; top:745px; width:349px; height:80px;">
    <svg viewBox="0 0 349 80" preserveAspectRatio="none" aria-hidden="true">
      <path d="M16,0 H333 L349,16 V64 L333,80 H16 L0,64 V16 Z" fill="var(--red)"/>
      <path d="M19,4 H330 L345,18 V62 L330,76 H19 L4,62 V18 Z" fill="none" stroke="var(--gold)" stroke-width="2"/>
    </svg>
    <p style="font-size:17px; line-height:1.25; padding:0 20px;">All wings are served with Blue Cheese or Ranch, Celery &amp; Carrots</p>
  </div>

  <!-- Burritos column -->
  <div class="brand">
    <span class="brand-mark"></span>
    <span class="brand-name">The Kettlebrook</span>
  </div>

  <div class="hours">
    <h3>Open Hours</h3>
    <p>Thurs, Friday &amp; Saturday<br>4 p.m&nbsp; to 12 a.m.</p>
  </div>

  <div class="ribbon" style="left:422px; top:310px; width:348px;">
    <svg viewBox="0 0 348 54" preserveAspectRatio="none" aria-hidden="true">
      <polygon points="0,14 40,14 40,50 0,50 12,32" fill="var(--red-dark)"/>
      <polygon points="348,14 308,14 308,50 348,50 336,32" fill="var(--red-dark)"/>
      <path d="M26,4 Q174,14 322,4 L322,42 Q174,52 26,42 Z" fill="var(--red)"/>
    </svg>
    <span>Burritos</span>
  </div>

  <div class="intro">
    <p>Build your own!</p>
    <p style="font-weight:700; font-size:12px;">Includes choice of meat, toppings &amp; side of salsa and chips</p>
    <p class="fresh">All Ingredients made fresh daily!</p>
  </div>

  <div class="section-title" style="left:422px; top:442px;">Meats</div>
  <div class="price-badge" style="left:745px; top:440px;">$</div>

  <div class="row" style="left:422px; top:491px; width:316px;"><span>Red Chile Grilled Chicken</span><span>9.00</span></div>
  <div class="desc" style="left:422px; top:510px;">Chicken marinated in a Red Chile Ancho sauce – this grilled chicken is the perfect blend of sassy, salty, savory and mild spice</div>
  <div class="row" style="left:422px; top:552px; width:316px;"><span>Spicy Shredded Beef</span><span>9.00</span></div>
  <div class="desc" style="left:422px; top:571px;">Slow cooked in a Chipotle Pepper sauce – saucy &amp; spicy</div>
  <div class="row" style="left:422px; top:598px; width:316px;"><span>Pork Carnitas</span><span>9.00</span></div>
  <div class="desc" style="left:422px; top:617px;">Wrapped in bacon and slow roasted – our pork is seasoned to perfection with subtle hints of clove and citrus</div>
  <div class="row" style="left:422px; top:656px; width:316px;"><span>Veggie</span><span>9.00</span></div>
  <div class="desc" style="left:422px; top:675px;">Wrap up your favorite combination of meat-free toppings to create a vegetarian delight (guac included )</div>

  <div class="section-title" style="left:422px; top:720px;">Personalize</div>
  <div class="list" style="left:422px; top:765px;">Cheddar Jack Cheese<br>Sour Cream<br>Black Beans</div>
  <div class="divider" style="left:627px; top:770px; height:62px;"></div>
  <div class="list" style="left:652px; top:765px;">Red Onion<br>Bacon<br>Medium Salsa</div>

  <!-- Extras & Drinks column -->
  <div class="list" style="left:822px; top:20px;">Refried Beans<br>Cilantro Lime Rice<br>Guacamole<small>(add $1.00)</small></div>
  <div class="divider" style="left:1009px; top:24px; height:76px;"></div>
  <div class="list" style="left:1056px; top:20px;">Pico de Gallo<small style="margin-bottom:3px;">(mild tomato salsa)</small>Hot Salsa<br>Lettuce</div>

  <div class="ribbon" style="left:822px; top:124px; width:355px;">
    <svg viewBox="0 0 355 54" preserveAspectRatio="none" aria-hidden="true">
      <polygon points="0,14 40,14 40,50 0,50 12,32" fill="var(--red-dark)"/>
      <polygon points="355,14 315,14 315,50 355,50 343,32" fill="var(--red-dark)"/>
      <path d="M26,4 Q177,14 329,4 L329,42 Q177,52 26,42 Z" fill="var(--red)"/>
    </svg>
    <span>Extras</span>
  </div>
  <div class="price-badge" style="left:1150px; top:194px;">$</div>
  <div class="row" style="left:822px; top:230px; width:355px;"><span>Basket of Chips &amp; Salsa</span><span>4.00</span></div>
  <div class="row" style="left:822px; top:254px; width:355px;"><span>Basket of Chips &amp; Guacamole</span><span>4.00</span></div>
  <div class="row" style="left:822px; top:278px; width:355px;"><span>Basket of Steak Fries</span><span>4.00</span></div>
  <div class="row" style="left:822px; top:302px; width:355px;"><span>Kids Basket of Fries &amp; Nuggets</span><span>5.00</span></div>
  <div class="row" style="left:822px; top:327px; width:355px;"><span>Deep Fried Smore</span><span>3.00</span></div>

  <div class="ribbon" style="left:822px; top:378px; width:355px;">
    <svg viewBox="0 0 355 54" preserveAspectRatio="none" aria-hidden="true">
      <polygon points="0,14 40,14 40,50 0,50 12,32" fill="var(--red-dark)"/>
      <polygon points="355,14 315,14 315,50 355,50 343,32" fill="var(--red-dark)"/>
      <path d="M26,4 Q177,14 329,4 L329,42 Q177,52 26,42 Z" fill="var(--red)"/>
    </svg>
    <span>Drinks</span>
  </div>
  <div class="price-badge" style="left:1150px; top:440px;">$</div>
  <div class="row" style="left:822px; top:475px; width:355px;"><span>Cola</span><span>3.00</span></div>
  <div class="row" style="left:822px; top:499px; width:355px;"><span>Diet Cola</span><span>3.00</span></div>
  <div class="row" style="left:822px; top:523px; width:355px;"><span>Lemon-Lime Soda</span><span>3.00</span></div>
  <div class="row" style="left:822px; top:547px; width:355px;"><span>Ginger Ale</span><span>3.00</span></div>
  <div class="row" style="left:822px; top:571px; width:355px;"><span>Citrus Rush</span><span>3.00</span></div>
  <div class="row" style="left:822px; top:596px; width:355px;"><span>Cherry Fizz</span><span>3.00</span></div>
  <div class="row" style="left:822px; top:620px; width:355px;"><span>Iced Tea</span><span>3.00</span></div>
  <div class="row" style="left:822px; top:644px; width:355px;"><span>Sweet Tea</span><span>3.00</span></div>
  <div class="row" style="left:822px; top:668px; width:355px;"><span>Kids Milk</span><span>1.50</span></div>
  <div class="row" style="left:822px; top:692px; width:355px;"><span>Kids Cranberry Juice</span><span>1.50</span></div>
  <div class="row" style="left:822px; top:717px; width:355px;"><span>Kids Apple Juice</span><span>1.50</span></div>
  <div class="row" style="left:822px; top:741px; width:355px;"><span>Kids Soda</span><span>1.50</span></div>
  <div class="row" style="left:822px; top:765px; width:355px;"><span>Coffee</span><span>1.50</span></div>
  <div class="row" style="left:822px; top:789px; width:355px;"><span>Hot Tea</span><span>1.50</span></div>
  <div class="row" style="left:822px; top:813px; width:355px;"><span>Hot Chocolate</span><span>1.50</span></div>
</div>
</body>
</html>
```